Brightmarrow HR - DL Postcard Fliers

I have a need to get some quotes to create a series of postcard fliers to promote my Human Resources Consultancy & Contracting services. I'd like to start with one to get a feel for how they might look when I introduce other products/services connected to my business. I think DL size would work best (99 x 210 mm). I have enclosed an A4 sheet that has a LOT of content. Would like it to be more visual and less wordy. Id like to feature my broader HR services on back side and the specific product/service offering on the front. For the first one, I would like the focus to be on recruitment. Perhaps need to highlight 20% off as an introductory rate off already cost effective flat rate structure for recruitment. Please keep punchy, less wordy. Happy to review some options you may done for someone else in the past and work with you on final content. Good luck.
Updates

Hi All. I am about 5 days away from making a decision now. I posted a request for an updated logo design last week and am waiting on submissions. Once i have decided on logo design, I will ask you to incorporate into your designs. It will have same coloring and not be too different so should be able to quickly incorporate into your designs. Thanks for your patience.

Target Market(s)

Small to medium enterprises

Industry/Entity Type

Quotes

Font styles to use
Serif

Colors
ec1f27

Requirements
Must have
• Contact Details - mobile, website, email
• Specifics on what product offering is and benefits
• A Call to action
• Ideally double sided DL - landscape view - one side with general information about the business generally, the other side with a specific focus on one product/service offering from within my business.
Should not have
• Too many words.

```html
<!DOCTYPE html>
<html lang="en">
<head>
<meta charset="utf-8">
<title>Brightmarrow HR – Recruitment Special</title>
<link rel="stylesheet" href="https://fonts.googleapis.com/css2?family=Oswald:wght@700&family=Lato:wght@400;700;900&display=swap">
<style>
  :root {
    --red: #ec1f27;
    --red-deep: #c8141b;
    --black: #0b0b0b;
    --ink: #3a3a3a;
    --white: #ffffff;
    --paper-top: #ffffff;
    --paper-bottom: #e4e4e4;
    --stage: #ececec;
    --photo-light: #e9eef3;
    --photo-mid: #b9c7d4;
  }
  html, body {
    margin: 0;
    width: 1200px;
    height: 786px;
    overflow: hidden;
    background: var(--stage);
  }
  .flyer {
    position: absolute;
    left: 70px;
    top: 135px;
    width: 1080px;
    height: 527px;
    overflow: hidden;
    font-family: "Lato", Arial, sans-serif;
    box-shadow: 0 2px 10px rgba(0,0,0,0.15);
  }
  .flyer__shapes { position: absolute; inset: 0; }
  .flyer__title {
    position: absolute;
    left: 37px;
    top: 30px;
    margin: 0;
    font-family: "Oswald", "Arial Narrow", sans-serif;
    font-weight: 700;
    font-size: 56px;
    line-height: 1;
    color: var(--red);
    transform: scaleX(0.88);
    transform-origin: left top;
    white-space: nowrap;
  }
  .flyer__tagline {
    position: absolute;
    left: 38px;
    top: 106px;
    width: 490px;
    margin: 0;
    font-weight: 900;
    font-size: 17px;
    line-height: 20px;
    color: var(--ink);
  }
  .flyer__intro {
    position: absolute;
    left: 46px;
    top: 214px;
    width: 505px;
    color: var(--white);
    font-size: 14px;
    line-height: 18px;
  }
  .flyer__intro p { margin: 0 0 8px; }
  .offer {
    font-weight: 900;
    font-size: 19px;
    line-height: 23px;
  }
  .offer__rate { font-size: 24px; }
  .package {
    position: absolute;
    top: 382px;
    margin: 0;
    padding: 0;
    list-style: none;
    color: var(--white);
    font-size: 14px;
    line-height: 17px;
  }
  .package--left { left: 44px; width: 275px; }
  .package--right { left: 364px; width: 290px; }
  .package li { position: relative; padding-left: 15px; }
  .package li::before {
    content: "";
    position: absolute;
    left: 0;
    top: 5px;
    width: 7px;
    height: 7px;
    border-radius: 50%;
    background: var(--white);
  }
  .cta {
    position: absolute;
    left: 780px;
    top: 398px;
    width: 270px;
    margin: 0;
    text-align: center;
    font-weight: 900;
    font-size: 15px;
    color: var(--red);
  }
  .brand {
    position: absolute;
    left: 780px;
    top: 423px;
    width: 270px;
    height: 56px;
    background: var(--white);
    display: flex;
    align-items: center;
    justify-content: center;
    gap: 10px;
  }
  .brand__mark { width: 20px; height: 20px; background: var(--red); }
  .brand__name {
    font-weight: 700;
    font-size: 26px;
    color: var(--red);
  }
  .contact {
    position: absolute;
    left: 770px;
    top: 486px;
    width: 290px;
    margin: 0;
    text-align: center;
    font-size: 12px;
    line-height: 15px;
    color: var(--ink);
  }
  .contact strong { font-weight: 900; color: var(--black); }
</style>
</head>
<body>
<article class="flyer">
  <svg class="flyer__shapes" width="1080" height="527" viewBox="0 0 1080 527">
    <defs>
      <linearGradient id="paper" x1="0" y1="0" x2="0" y2="1">
        <stop offset="0" stop-color="#ffffff"/>
        <stop offset="1" stop-color="#e4e4e4"/>
      </linearGradient>
      <linearGradient id="photoTone" x1="0" y1="0" x2="1" y2="1">
        <stop offset="0" stop-color="#b9c7d4"/>
        <stop offset="0.5" stop-color="#e9eef3"/>
        <stop offset="1" stop-color="#cfd9e2"/>
      </linearGradient>
      <linearGradient id="redTone" x1="0" y1="0" x2="0" y2="1">
        <stop offset="0" stop-color="#ec1f27"/>
        <stop offset="1" stop-color="#c8141b"/>
      </linearGradient>
    </defs>

    <rect class="paper" width="1080" height="527" fill="url(#paper)"/>

    <path class="team-photo" role="img" aria-label="Photo of four smiling business professionals in an office"
          d="M590 0 L1080 0 L1080 372 L742 372 Q716 372 706 342 Z" fill="url(#photoTone)"/>

    <path class="photo-rule" d="M572 0 L694 352 Q706 388 748 388 L1080 388"
          fill="none" stroke="#0b0b0b" stroke-width="9"/>

    <polygon class="edge-stripe" points="542,0 560,0 744,527 726,527" fill="#0b0b0b"/>

    <path class="info-block" d="M0 178 L530 178 Q575 178 590 222 L705 527 L0 527 Z" fill="#0b0b0b"/>

    <path class="intro-panel" role="img" aria-label="Red-tinted city skyline behind the introduction text"
          d="M0 198 L525 198 Q565 198 578 236 L620 358 L0 358 Z"
          fill="url(#redTone)" stroke="#ffffff" stroke-width="4"/>
  </svg>

  <h1 class="flyer__title">RECRUITMENT SPECIAL</h1>
  <p class="flyer__tagline">PEOPLE ARE YOUR BEST ASSET, RIGHT? …NO, THE RIGHT PEOPLE ARE!!!!</p>

  <div class="flyer__intro">
    <p class="offer">INTRODUCTORY OFFER: <span class="offer__rate">20% OFF</span><br>our already cost-effective flat rate</p>
    <p>Hire right, first time. Save money, effort and time with less turnover and lower rehiring &amp; training costs, and build better teams sooner. Our Recruitment Package includes…</p>
  </div>

  <ul class="package package--left">
    <li>On Site Review of your Business in relation to the role</li>
    <li>Clarification around Position Requirements</li>
    <li>Advertised through multiple channels and networks</li>
    <li>Screening of CV and Cover Letter</li>
  </ul>
  <ul class="package package--right">
    <li>Phone Screen Interviews</li>
    <li>Face to face Interviews</li>
    <li>On Line Assessments (where applicable)</li>
    <li>Background Reference Checks</li>
    <li>4 Month Warranty</li>
  </ul>

  <p class="cta">CALL TODAY – START HIRING RIGHT!</p>
  <div class="brand">
    <span class="brand__mark"></span>
    <span class="brand__name">Brightmarrow HR</span>
  </div>
  <p class="contact"><strong>M</strong> 0400 123 456 &nbsp;·&nbsp; <strong>W</strong> brightmarrowhr.com<br><strong>E</strong> hello@brightmarrowhr.com</p>
</article>
</body>
</html>
```